Relaunch of company website (Technical company)

Hi all,

we need a website based on Wordpress who makes the customer curious and excited of all the possibilities we can offer.
Customers are B2B. The layout should be based on the screenshots I added, but refreshed and modernized with some nice gadgets.
All needs to be responsive for the different devices.
We are a technical company. We provide a full range of service from 3D scan, Manufacturing, Prototyping, Bulk production and CAD service.

Later the website needs to have a multi language option.

Home:

1. Logo top left (attached)
2. Menu bar top right
3. Header picture like in the screenshot
4. Than the three small blue pics (CAD - Fertigung - Manufaktur) we want a
hoover-small zoom effect as soon as the mouse hits them.
5. Introduction text of our company
6. Contact Information (Design sample see attachment)
7. At the end "Impressum - Datenschutzerklärung - Haftungsausschluss. Those need to be linked to extra pages where we can add mandatory text (Legal notice, Privacy, Disclaimer)

Leistungen - Our service:

1. See the attachment named our service.
2. First on page a gallery where we can add pictures. If moving the mouse over the picture we want a one line explanation e.g. 3D Scan, Production, Die cast...
no click option at the pictures, just to see.
3. Below that, a side menu (we need to add or remove items by our self if necessary) on the left where we can add our service.
4. If the customer is clicking a service, it needs to be highlighted
5. After clicking a service we want our text to that service appear right of the menu (see attachment sample) and 2 big pictures on top of the menu and text field.

Gallery:

1. Headline pictures for each gallery Category (6-8 at the moment)
2. Mouse over the picture zooms it a little in and adds a text what category it is
e.g. Reverse engineering, Prototyping, Laserscan
3. Clicking on the picture opens the detail gallery to that category. There we need
to add pictures specific to that service.
4. If the customer is clicking on a picture from there, all pictures from that
Category will open in a full screen view mode

Blog:

1. A blog to add news (picture and text). Right now we don´t have the time to feed
it, so we want to deactivate it as long as we cant keep it up to date. Later it
should be part of the website.

Unternehmen:

1. Drop down menu: Our Team - History - Unsere Partner - AGB - Impressum

Our Team:
1. Short description of our employees including picture (see attachment)
2. Contact Information (Design sample see attachment)
3. At the end "Impressum - Datenschutzerklärung - Haftungsausschluss. Those need to be linked to extra pages where we can add mandatory text (Legal notice, Privacy, Disclaimer)

History:
1. Timeline where we can add milestones including date, and pictures of the company (see screenshot)

Unsere Partner:
1. Text field where we can introduce our partners including pictures if necessary.

A blog would be a nice option, social media shortcuts to Lumigrid-QZ but no preview of QZ Timeline within the website.

We do have professional text already, that will be added by us. We expect you to use any sample text and pictures for the draft, beside what we supply already.

If you see the need of buying pictures from Pixvane or any other picture company that is OK for us.

What we expect:

A modern, fresh website based on our existing design, changes are fine as long as the whole website design does not change completely to an unicorn thing in pink. Feel free to be creative. New ideas will be discussed, we are open to good ideas. We don´t stick fix to our idea, but we want our customers can see that its still the same company.
Scrolling effects would be a nice gadget if possible.

We have a bad page already...don´t want a second bad one :-)

Our company blue is RBG 106, 206, 224

Greets to all, looking for professional results.

Target Market(s)

B2B, Engineering companys,

Industry/Entity Type

Technical Service

Number of Pages Required

5+ page

Font styles to use
Sans Serif
Other font styles liked:
• verdana

Colors
0455a3
000000
ffffff

Requirements
Must have
• Responsive design, We want to be able to add posts to the Blog, pictures to the categories, and categories by ourself if necessary. (Wordpress)
• Lets say we want to add one more category at „Leistungen-Our Service“ that should be possible for us in the wordpress background.
Nice to have
• Dynamic elements to make the website more alive.
Should not have
• Sliders, Contact form

```html
<!DOCTYPE html>
<html lang="de">
<head>
<meta charset="utf-8">
<title>Norvek Precision</title>
<link href="https://fonts.googleapis.com/css2?family=Questrial&display=swap" rel="stylesheet">
<style>
:root{
  --blue:#0f7fc2;
  --blue-light:#2a9de2;
  --blue-dark:#0c5f95;
  --ink:#1a1a1a;
  --text:#333;
  --white:#fff;
  --grey-hero-a:#4d4d4d;
  --grey-hero-b:#7a7a7a;
}
*{margin:0;padding:0;box-sizing:border-box}
html,body{width:788px;height:1200px;overflow:hidden;background:var(--white)}
body{font-family:"Questrial",Verdana,sans-serif;color:var(--text);position:relative}
a{color:inherit;text-decoration:none}

.topbar{position:absolute;left:0;top:0;width:788px;height:26px;background:var(--blue);color:var(--white);font-size:10px}
.topbar span{position:absolute;top:7px;display:flex;align-items:center;gap:4px;white-space:nowrap}
.topbar .sep{position:absolute;top:0;width:1px;height:26px;background:rgba(255,255,255,.35)}

.nav{position:absolute;top:26px;left:0;width:788px;height:56px;background:var(--white)}
.brand{position:absolute;left:93px;top:10px;font-size:19px;line-height:1;color:var(--ink);letter-spacing:.5px;border-bottom:1px solid var(--ink);padding-bottom:2px}
.menu{position:absolute;top:23px;font-size:9.5px;color:var(--ink);letter-spacing:.3px;white-space:nowrap}
.menu.active{color:var(--blue);border-bottom:1px solid var(--blue);padding-bottom:2px}

.hero{position:absolute;top:82px;left:0;width:788px;height:308px;background:linear-gradient(120deg,var(--grey-hero-a),var(--grey-hero-b) 50%,var(--grey-hero-a))}
.hero-card{position:absolute;left:93px;top:44px;width:291px;height:220px;background:var(--white);border-radius:6px;padding:10px}
.hero-card .ph{width:100%;height:100%;background:radial-gradient(circle at 50% 50%,#c9c9c9,#f2f2f2 70%);border-radius:3px}
.hero h1{position:absolute;left:405px;top:98px;font-weight:400;font-size:26px;color:var(--ink);border-bottom:1.5px solid var(--ink);line-height:1.1;padding-bottom:2px;white-space:nowrap}
.hero p{position:absolute;left:405px;top:140px;width:275px;font-size:9.6px;line-height:1.35;color:var(--white)}
.btn{position:absolute;background:var(--blue-light);color:var(--white);font-size:8.5px;border-radius:12px;display:flex;align-items:center;justify-content:center}
.dots{position:absolute;left:465px;display:flex;align-items:center;gap:8px}
.dots i{display:block;width:6px;height:6px;border-radius:50%;background:var(--blue-light)}

.service{position:absolute;top:436px;width:191px;height:152px;padding:18px 19px}
.service.card{background:var(--white);box-shadow:0 0 5px rgba(0,0,0,.15)}
.service h3{font-weight:400;font-size:9px;color:var(--ink);margin-top:10px}
.service p{font-size:7px;line-height:1.65;margin-top:12px;color:var(--text)}
.service a{display:inline-block;margin-top:12px;font-size:8px;color:var(--blue);text-decoration:underline}

.about h2{position:absolute;left:94px;top:658px;font-weight:400;font-size:16px;color:var(--ink);border-bottom:1px solid var(--ink);padding-bottom:3px;white-space:nowrap}
.about .lead{position:absolute;left:94px;top:695px;font-size:9.5px;color:var(--blue)}
.about p{position:absolute;left:94px;width:285px;font-size:9.5px;line-height:1.38;color:var(--ink)}
.about ul{position:absolute;left:94px;top:844px;list-style:none;font-size:9.5px;color:var(--ink)}
.about li{display:flex;align-items:center;gap:10px;margin-bottom:5px}
.about li::before{content:"";width:5px;height:5px;border-radius:50%;background:var(--blue)}
.about-back{position:absolute;left:408px;top:654px;width:269px;height:279px;background:var(--blue)}
.about-img{position:absolute;left:426px;top:636px;width:269px;height:278px;background:linear-gradient(160deg,#ffffff,#e6e6e6 55%,#bdbdbd);box-shadow:0 0 4px rgba(0,0,0,.12)}

.footer{position:absolute;top:979px;left:0;width:788px;height:136px;background:var(--blue);color:var(--white)}
.fcol{position:absolute;top:24px;font-size:7.3px}
.fcol h4{font-weight:400;font-size:8.3px;border-bottom:1px solid rgba(255,255,255,.8);padding-bottom:3px;display:inline-block;margin-bottom:9px}
.fcol li{list-style:none;line-height:13.3px}
.contact li{display:flex;gap:9px;line-height:13px;margin-bottom:6px}
.fbrand{position:absolute;left:588px;top:38px;font-size:18px;line-height:1;border-bottom:1px solid var(--white);padding-bottom:2px}

.band{position:absolute;top:1115px;left:0;width:788px;height:55px;background:var(--blue-dark);color:var(--white)}
.social{position:absolute;left:94px;top:22px;display:flex;gap:9px;font-size:7.5px}
.band h5{position:absolute;left:268px;top:19px;font-weight:400;font-size:12.5px;white-space:nowrap}
.signup{position:absolute;left:464px;top:17px;width:231px;height:22px;background:var(--white);border-radius:11px;font-size:7px;color:#aaa;padding:7px 16px}
.signup svg{position:absolute;right:9px;top:6px}
.copy{position:absolute;top:1170px;left:0;width:788px;height:30px;background:var(--blue);color:var(--white);font-size:7.3px;text-align:center;line-height:30px}
</style>
</head>
<body>

<header>
  <div class="topbar">
    <span style="left:421px"><svg width="9" height="9" viewBox="0 0 10 10"><path d="M2 0l2 2.5-1.2 1.2c.6 1.4 1.6 2.4 3 3L7 5.5 9.6 7.6 8.4 9.7C4 9.5.5 6 .3 1.6z" fill="#fff"/></svg>555.014.2290</span>
    <div class="sep" style="left:502px"></div>
    <span style="left:513px"><svg width="10" height="8" viewBox="0 0 10 8"><rect width="10" height="8" rx="1" fill="#fff"/><path d="M0 .5l5 3.5 5-3.5" stroke="#0f7fc2" fill="none"/></svg>info@norvekmfg.com</span>
    <div class="sep" style="left:638px"></div>
    <span style="left:647px">ENGLISH <svg width="8" height="5" viewBox="0 0 8 5"><path d="M1 1l3 3 3-3" stroke="#fff" stroke-width="1.4" fill="none"/></svg></span>
  </div>
  <nav class="nav">
    <div class="brand">Norvek<br>PRECISION</div>
    <a class="menu active" style="left:334px">HOME</a>
    <a class="menu" style="left:398px">LEISTUNGEN</a>
    <a class="menu" style="left:486px">GALLERY</a>
    <a class="menu" style="left:559px">BLOG</a>
    <a class="menu" style="left:620px">UNTERNEHMEN <svg width="8" height="5" viewBox="0 0 8 5"><path d="M1 1l3 3 3-3" stroke="#1a1a1a" stroke-width="1.4" fill="none"/></svg></a>
  </nav>
</header>

<section class="hero">
  <div class="hero-card"><div class="ph" role="img" aria-label="Exploded 3D render of an electric motor assembly"></div></div>
  <h1>NORVEK PRECISION</h1>
  <p>Lorem ipsum dolor sit amet, consectetuer adipiscing elit, sed diam nonummy nibh euismod tincidunt ut laoreet dolore magna aliquam erat volutpat. Ut wisi enim.</p>
  <a class="btn" style="left:405px;top:185px;width:77px;height:23px">LEARN MORE</a>
  <div class="dots" style="top:266px">
    <i></i><i></i><i></i>
    <span style="width:16px;height:1px;background:var(--blue-light);margin:0 4px"></span>
    <svg width="16" height="16" viewBox="0 0 16 16"><circle cx="8" cy="8" r="6" fill="none" stroke="#2a9de2" stroke-width="3"/></svg>
    <span style="font-size:7.5px;color:var(--blue-light)">01 / 05</span>
    <svg width="10" height="12" viewBox="0 0 10 12" style="margin-left:12px"><path d="M8 1L3 6l5 5" stroke="#2a9de2" stroke-width="1.8" fill="none"/></svg>
    <svg width="10" height="12" viewBox="0 0 10 12"><path d="M2 1l5 5-5 5" stroke="#2a9de2" stroke-width="1.8" fill="none"/></svg>
  </div>
</section>

<section class="services">
  <div class="service card" style="left:93px">
    <svg width="42" height="28" viewBox="0 0 42 28"><path d="M1 27L9 1l8 26M13 27L21 1l8 26M25 27L33 1l8 26" stroke="#0f7fc2" stroke-width="2.5" fill="none"/></svg>
    <h3>CAD SERVICE</h3>
    <p>Lorem ipsum dolor sit amet, consectetuer adipiscing elit, sed diam nonummy nibh euismod tincidunt ut laoreet dolore magna.</p>
    <a>LEARN MORE</a>
  </div>
  <div class="service" style="left:299px">
    <svg width="36" height="28" viewBox="0 0 36 28"><circle cx="12" cy="17" r="8" fill="none" stroke="#0f7fc2" stroke-width="5" stroke-dasharray="3 2"/><circle cx="12" cy="17" r="6" fill="#0f7fc2"/><circle cx="12" cy="17" r="2.5" fill="#fff"/><circle cx="27" cy="8" r="5.5" fill="none" stroke="#0f7fc2" stroke-width="4" stroke-dasharray="2.5 1.8"/><circle cx="27" cy="8" r="4" fill="#0f7fc2"/><circle cx="27" cy="8" r="1.8" fill="#fff"/></svg>
    <h3>FERTIGUNG</h3>
    <p>Lorem ipsum dolor sit amet, consectetuer adipiscing elit, sed diam nonummy nibh euismod tincidunt ut laoreet dolore magna.</p>
    <a>LEARN MORE</a>
  </div>
  <div class="service" style="left:504px">
    <svg width="34" height="28" viewBox="0 0 34 28"><path d="M2 8h24v19H2zM2 8l6-6h24l-6 6M26 27l6-6V2" stroke="#0f7fc2" stroke-width="2" fill="none" stroke-linejoin="round"/><path d="M26 8l6-6v19l-6 6z" fill="#0f7fc2"/></svg>
    <h3>MANUFAKTUR</h3>
    <p>Lorem ipsum dolor sit amet, consectetuer adipiscing elit, sed diam nonummy nibh euismod tincidunt ut laoreet dolore magna.</p>
    <a>LEARN MORE</a>
  </div>
</section>

<section class="about">
  <h2>ABOUT NORVEK PRECISION</h2>
  <div class="lead">Lorem ipsum dolor sit amet</div>
  <p style="top:711px">consectetuer adipiscing elit, sed diam nonummy nibh euismod tincidunt ut laoreet dolore magna aliquam erat volutpat.</p>
  <p style="top:745px">Ut wisi enim ad minim veniam, quis nostrud exerci tation ullamcorper suscipit lobortis nisl ut aliquip ex ea commodo consequat. Duis autem vel eum iriure dolor in hendrerit in vulputate velit esse molestie consequat, vel illum dolore eu feugiat nulla facilisis at vero eros et accumsan et iusto odio dignissim qui blandit praesent luptatum zzril delenit augue duis dolore te feugait nulla facilisi.</p>
  <ul>
    <li>Ut wisi enim ad minim veniam, quis nostrud</li>
    <li>vero eros et accumsan et iusto odio</li>
  </ul>
  <a class="btn" style="left:93px;top:886px;width:77px;height:22px">LEARN MORE</a>
  <div class="about-back"></div>
  <div class="about-img" role="img" aria-label="Machined steel gear part resting on a technical drawing"></div>
</section>

<footer>
  <div class="footer">
    <div class="fcol" style="left:94px"><h4>QUICK LINKS</h4><ul><li>Home</li><li>Leistungen</li><li>Gallery</li><li>Blog</li><li>Unternehmen</li></ul></div>
    <div class="fcol" style="left:197px"><h4>OTHER LINKS</h4><ul><li>CAD</li><li>Fertigung</li><li>Manufaktur</li></ul></div>
    <div class="fcol" style="left:299px"><h4>INFORMATION LINKS</h4><ul><li>Impressum</li><li>Datenschutzerklärung</li><li>Haftungsausschluss</li></ul></div>
    <div class="fcol contact" style="left:431px"><h4>CONTACT US</h4><ul>
      <li><svg width="7" height="9" viewBox="0 0 7 9"><path d="M3.5 9S0 5 0 3.5a3.5 3.5 0 017 0C7 5 3.5 9 3.5 9z" fill="#fff"/><circle cx="3.5" cy="3.5" r="1.3" fill="#0f7fc2"/></svg><span>Lorem ipsum dolor<br>72 Harbor Row Lorem 654321</span></li>
      <li><svg width="8" height="8" viewBox="0 0 10 10"><path d="M2 0l2 2.5-1.2 1.2c.6 1.4 1.6 2.4 3 3L7 5.5 9.6 7.6 8.4 9.7C4 9.5.5 6 .3 1.6z" fill="#fff"/></svg><span>555.014.2290</span></li>
      <li><svg width="9" height="7" viewBox="0 0 10 8"><rect width="10" height="8" rx="1" fill="#fff"/><path d="M0 .5l5 3.5 5-3.5" stroke="#0f7fc2" fill="none"/></svg><span>info@norvekmfg.com</span></li>
    </ul></div>
    <div class="fbrand">Norvek<br>PRECISION</div>
  </div>
  <div class="band">
    <div class="social"><span>QZ</span><span>Corvo</span><span>Lumigrid</span><span>Linkra</span></div>
    <h5>SIGN UP TO OUR NEWSLETTER</h5>
    <div class="signup">Enter your email address...<svg width="14" height="8" viewBox="0 0 14 8"><path d="M0 4h13M9 1l3.5 3L9 7" stroke="#0f7fc2" stroke-width="1.2" fill="none"/></svg></div>
  </div>
  <div class="copy">Copyright @ 2018 NORVEK PRECISION. All Rights Reserved.</div>
</footer>

</body>
</html>
```